Business card design to suit our website

Need a nice looking business card for our business based off images from our Website and provided images. The business card will require 2 different names (for the 2 owners). The business card should include images from our website, facebook (larkvale coil starter pack) or the pictures provided. it should also contain all contact information.
Our website is www.larkvalecoilworks.com.au
Please dont use image from top bar of website. If images are used please use the ones of our product under the buy it now tab
Updates

Need extra days to review

Target Market(s)

Automotive

Industry/Entity Type

Automotive Part

Contact Information for Business Card

Business Name. contact details including names phone number email. logo
2 business cards needed with 2 different persons names and phone number.

Colors

Designer to choose colors to be used in the design.

Requirements
Must have
• whatever looks best

```html
<!DOCTYPE html>
<html lang="en">
<head>
<meta charset="utf-8">
<title>Larkvale business card</title>
<link href="https://fonts.googleapis.com/css2?family=Questrial&family=Montserrat:wght@500;800&display=swap" rel="stylesheet">
<style>
  :root {
    --page: #ecebe7;
    --card: #1c1c1e;
    --streak-warm: #5a2a1e;
    --streak-cool: #24324a;
    --red: #e8363a;
    --white: #ffffff;
    --soft: #d9d9d9;
    --badge: #f2a31b;
  }
  * { margin: 0; padding: 0; box-sizing: border-box; }
  html, body { width: 1200px; height: 886px; overflow: hidden; background: var(--page); }
  body { position: relative; font-family: "Questrial", sans-serif; color: var(--white); }

  .card {
    position: absolute; left: 280px; width: 640px; height: 366px;
    background: var(--card); overflow: hidden;
    box-shadow: 0 6px 18px rgba(0,0,0,.18);
  }
  .card--front { top: 40px; }
  .card--back { top: 470px; }

  .card__backdrop {
    position: absolute; inset: 0;
    background:
      linear-gradient(172deg, transparent 18%, rgba(200,80,40,.55) 30%, transparent 40%),
      linear-gradient(176deg, transparent 38%, rgba(80,110,170,.45) 46%, transparent 54%),
      linear-gradient(180deg, var(--streak-warm) 0%, var(--card) 45%, var(--streak-cool) 62%, var(--card) 85%);
    opacity: .85;
  }
  .card--back .card__backdrop { opacity: .45; }

  .bar { position: absolute; height: 9px; background: var(--red); }
  .bar--top { top: 0; left: 0; width: 36%; }
  .bar--bottom { bottom: 0; right: 0; width: 36%; }

  .badge {
    position: absolute; top: 22px; right: 30px; width: 74px; height: 74px;
    border-radius: 50%; background: var(--badge);
  }

  .brand {
    font-family: "Montserrat", sans-serif; font-weight: 800; color: var(--white);
    letter-spacing: .5px;
  }
  .card--front .brand { position: absolute; left: 120px; top: 130px; font-size: 58px; }
  .product { position: absolute; left: 170px; top: 206px; font-size: 40px; color: var(--white); }

  .web {
    position: absolute; right: 30px; bottom: 28px; text-align: right;
    font-family: "Montserrat", sans-serif; font-weight: 500; color: var(--red);
    font-size: 22px; line-height: 1.05;
  }
  .web span { display: block; }

  .name-band {
    position: absolute; top: 42px; left: 290px; right: 0; height: 36px;
    background: var(--red); padding: 6px 14px;
    font-family: "Montserrat", sans-serif; font-size: 18px; font-weight: 500; text-transform: uppercase;
  }
  .name-band .role { text-transform: none; font-family: "Questrial", sans-serif; font-size: 17px; }

  .card--back .brand { position: absolute; left: 40px; top: 68px; font-size: 42px; }

  .contact { position: absolute; left: 302px; top: 92px; font-size: 16px; color: var(--soft); line-height: 1.3; }

  .address { position: absolute; font-size: 13px; color: var(--soft); line-height: 1.45; }
  .address h3 { font-family: "Montserrat", sans-serif; font-weight: 500; font-size: 15px; color: var(--white); margin-bottom: 4px; }
  .address--first { left: 40px; top: 176px; }
  .address--second { left: 302px; top: 150px; }
</style>
</head>
<body>
  <section class="card card--front">
    <div class="card__backdrop" role="img" aria-label="Photo of motion-blurred red and blue light streaks at night"></div>
    <div class="bar bar--top"></div>
    <div class="bar bar--bottom"></div>
    <div class="badge" role="img" aria-label="Made in Australia badge"></div>
    <div class="brand">Larkvale</div>
    <div class="product">coil starter pack</div>
    <div class="web"><span>www.</span><span>larkvalecoilworks</span><span>com.au</span></div>
  </section>

  <section class="card card--back">
    <div class="card__backdrop" role="img" aria-label="Photo of motion-blurred light streaks at night"></div>
    <div class="bar bar--top"></div>
    <div class="bar bar--bottom"></div>
    <div class="name-band">Your Name <span class="role">(Designation)</span></div>
    <div class="brand">Larkvale</div>
    <div class="contact">
      <p>Mobile number goes here</p>
      <p>Email id number goes here</p>
    </div>
    <div class="address address--first">
      <h3>1st office address</h3>
      <p>xxxxxxxxxxxxxxxxxxxxxxxxxxxxxxxxxx</p>
      <p>xxxxxxxxxxxxxxxxxxxxxxxxxxxxxxxxxx</p>
      <p>xxxxxxxxxxxxxxxxxxxxxxxxxxxxxxxxxx</p>
      <p>xxxxxxxxxxxxxxxxxxxxxxxxxxxxxxxxxx</p>
      <p>xxxxxxxxxxxxxxxxxxxxxxxxxxxxxxxxxx</p>
    </div>
    <div class="address address--second">
      <h3>2nd office address</h3>
      <p>xxxxxxxxxxxxxxxxxxxxxxxxxxxxxxxxxxxxxx</p>
      <p>xxxxxxxxxxxxxxxxxxxxxxxxxxxxxxxxxxxxxx</p>
      <p>xxxxxxxxxxxxxxxxxxxxxxxxxxxxxxxxxxxxxx</p>
      <p>xxxxxxxxxxxxxxxxxxxxxxxxxxxxxxxxxxxxxx</p>
      <p>xxxxxxxxxxxxxxxxxxxxxxxxxxxxxxxxxxxxxx</p>
    </div>
  </section>
</body>
</html>
```